Kestrel Ledger Stationary
Business cards and MS Word letterhead template
Creative Brief
Use same font as used in my logo
Bank Gothic
Modern
Marcus Bellweather
Chief Operating Officer
4826 N Halvern RD, STE 212 Tempe, AZ 85291
marcus.bellweather@kestrelledger.example
www.kestrelledger.example
Stationary requirements: MS Word template with logo, address and phone in the header. Vector graphics Color and grayscale
Logo or other design element and the following text: "Kestrel Ledger, LLC is a registered ISO/MSP of Harwick Savings and Loan."

```html
<!DOCTYPE html>
<html lang="en">
<head>
<meta charset="utf-8">
<title>Kestrel Ledger Stationery Concepts</title>
<link href="https://fonts.googleapis.com/css2?family=Michroma&family=Roboto:wght@400;500&display=swap" rel="stylesheet">
<style>
:root{
  --blue:#3f62ad;
  --blue-dark:#2f4d90;
  --grey:#8c8c8c;
  --grey-dark:#545454;
  --paper:#ffffff;
  --ground:#ece8e2;
  --ink:#3a3a3a;
  --faint:#e6ebf4;
}
*{box-sizing:border-box;margin:0;padding:0}
html,body{width:1200px;height:446px;overflow:hidden}
body{background:var(--ground);position:relative;font-family:"Roboto",Arial,sans-serif;color:var(--ink)}
.piece{position:absolute;background:var(--paper);box-shadow:0 1px 4px rgba(0,0,0,.25);overflow:hidden}
.piece svg.art{position:absolute;inset:0;width:100%;height:100%}
.label{position:absolute;font-family:"Michroma",Arial,sans-serif;font-size:5px;letter-spacing:.6px;text-transform:uppercase;color:#555}
.wordmark{font-family:"Michroma",Arial,sans-serif;color:var(--blue);white-space:nowrap;display:flex;align-items:center;gap:4px;position:absolute}
.wordmark .dot{display:inline-block;background:var(--blue)}
.wordmark.light{color:#fff}
.wordmark.light .dot{background:#fff}
.faint-square{position:absolute;background:var(--faint)}
.small{position:absolute;font-size:3.4px;line-height:1.45;color:#555}
</style>
</head>
<body>

<div class="label" style="left:12px;top:129px">Stationery Concepts</div>

<!-- Business card front -->
<section class="piece card-front" style="left:12px;top:149px;width:96px;height:62px">
  <div class="wordmark" style="left:6px;top:6px;font-size:5.5px"><span class="dot" style="width:6px;height:6px"></span>KESTREL LEDGER</div>
  <svg class="art" viewBox="0 0 96 62" aria-hidden="true"><path d="M70 62 C82 50 90 40 96 26 L96 62 Z" fill="var(--blue)"/><path d="M62 62 C76 52 86 42 92 28" stroke="var(--grey)" stroke-width="2" fill="none"/></svg>
  <div class="small" style="left:6px;top:30px">Marcus Bellweather<br>Chief Operating Officer<br>4826 N Halvern RD, STE 212 Tempe, AZ 85291<br>marcus.bellweather@kestrelledger.example<br>www.kestrelledger.example</div>
</section>
<div class="label" style="left:12px;top:214px">Business Card Front</div>

<!-- Business card back -->
<section class="piece card-back" style="left:12px;top:240px;width:96px;height:62px;background:var(--grey-dark)">
  <div class="wordmark light" style="left:16px;top:26px;font-size:5.5px"><span class="dot" style="width:6px;height:6px"></span>KESTREL LEDGER</div>
</section>
<div class="label" style="left:12px;top:305px">Business Card Back</div>

<!-- Letterhead option 1 -->
<section class="piece letterhead-1" style="left:163px;top:19px;width:293px;height:384px">
  <svg class="art" viewBox="0 0 293 384" preserveAspectRatio="none" aria-hidden="true">
    <path d="M250 0 C290 100 290 260 240 384 L293 384 L293 0 Z" fill="var(--blue)"/>
    <path d="M240 0 C278 100 278 260 228 384" stroke="var(--grey)" stroke-width="5" fill="none"/>
  </svg>
  <div class="wordmark" style="left:20px;top:18px;font-size:9px"><span class="dot" style="width:10px;height:10px"></span>KESTREL LEDGER</div>
  <div class="faint-square" style="left:96px;top:140px;width:80px;height:80px"></div>
  <div class="small" style="left:112px;top:340px;font-size:3.6px">Kestrel Ledger, LLC<br>4826 N Halvern RD, STE 212 Tempe, AZ 85291<br>www.kestrelledger.example<br>Kestrel Ledger, LLC is a registered ISO/MSP of Harwick Savings and Loan.</div>
</section>
<div class="label" style="left:250px;top:410px">Letterhead Option 1</div>

<!-- Letterhead option 2 -->
<section class="piece letterhead-2" style="left:480px;top:19px;width:300px;height:384px">
  <svg class="art" viewBox="0 0 300 384" preserveAspectRatio="none" aria-hidden="true">
    <path d="M0 384 C60 330 200 320 300 300 L300 384 Z" fill="var(--blue)"/>
    <path d="M0 370 C70 320 200 310 300 286" stroke="var(--grey)" stroke-width="6" fill="none"/>
    <path d="M0 384 C80 350 200 345 300 330 L300 384 Z" fill="var(--blue-dark)" opacity=".6"/>
  </svg>
  <div class="wordmark" style="left:22px;top:18px;font-size:9px"><span class="dot" style="width:10px;height:10px"></span>KESTREL LEDGER</div>
  <div class="faint-square" style="left:106px;top:140px;width:80px;height:80px"></div>
</section>
<div class="label" style="left:585px;top:410px">Letterhead Option 2</div>

<!-- Envelope option 1 -->
<section class="piece envelope-1" style="left:792px;top:24px;width:384px;height:101px">
  <svg class="art" viewBox="0 0 384 101" preserveAspectRatio="none" aria-hidden="true"><path d="M0 0 H384 V28 C300 50 84 50 0 28 Z" fill="var(--blue)"/></svg>
  <span style="position:absolute;left:184px;top:46px;width:16px;height:16px;background:var(--blue)"></span>
</section>

<!-- Envelope option 2 -->
<section class="piece envelope-2" style="left:792px;top:149px;width:384px;height:91px">
  <svg class="art" viewBox="0 0 384 91" preserveAspectRatio="none" aria-hidden="true"><path d="M0 0 H384 V26 C300 46 84 46 0 26 Z" fill="var(--grey-dark)"/></svg>
  <span style="position:absolute;left:184px;top:48px;width:16px;height:16px;background:var(--grey)"></span>
</section>

<!-- Envelope option 3 -->
<section class="piece envelope-3" style="left:792px;top:259px;width:384px;height:77px">
  <svg class="art" viewBox="0 0 384 77" preserveAspectRatio="none" aria-hidden="true"><path d="M0 50 C100 70 284 70 384 50 V77 H0 Z" fill="var(--blue)"/></svg>
  <span style="position:absolute;left:184px;top:18px;width:16px;height:16px;background:var(--blue)"></span>
</section>

<!-- Long envelope -->
<section class="piece envelope-long" style="left:797px;top:350px;width:379px;height:77px">
  <svg class="art" viewBox="0 0 379 77" preserveAspectRatio="none" aria-hidden="true">
    <path d="M250 77 C300 70 350 50 379 30 V77 Z" fill="var(--blue)"/>
    <path d="M230 77 C290 68 345 46 379 22" stroke="var(--grey)" stroke-width="3" fill="none"/>
  </svg>
  <div class="wordmark" style="left:12px;top:10px;font-size:6.5px"><span class="dot" style="width:7px;height:7px"></span>KESTREL LEDGER</div>
</section>
<div class="label" style="left:940px;top:432px">Envelope Option 3</div>

</body>
</html>
```